Bureau for Venture and Discovery Needs a Graphically Designed Powerpoint Template

We are from Bureau for Venture and Discovery (BVaD), part of a medical school. BVaD contributes to the medical school by overseeing and managing intellectual property generated by researchers at the medical school, and also works to ensure optimal commercial outcomes for all inventions arising from the medical school. We want a graphically designed powerpoint presentation template to describe how BVaD is involved in a researcher’s journey to major scientific contributions. The journey should be represented in the form of a main road (or pathway). Along the main road, there will be smaller roads branching out, each representing one of the researcher’s major scientific contributions. We will be inputting text details of each major scientific contribution near each of the small road branches. The smaller road branches will also need to be removable / editable. This is because we might need to send the template to different researchers to input details of their major scientific contributions, and each researcher will have a different number of them. Hence, you can possibly place around 6 branches along the main road, but we want to be able to remove the branches should we need to. Removal of the branches (design elements) should still result in a seamless image in powerpoint. We also want to be able to add and edit text in the design template. The start of the main road should contain a placeholder for us to place the researcher’s photo. The end of the road will lead to one of the major scientific contributions. Please see the uploaded sketch to have an idea of what we are looking to get. We welcome deviations and changes to the design as shown from the sketch, as long as the design is able to convey what we have described above. As this powerpoint template will be used for presentation to the senior management, we need it to look beautiful yet professional.

Target Market(s)

Researcher, Scientist

Industry/Entity Type

School

Font styles to use
Serif
Sans Serif

Requirements
Must have
• A main road or pathway as mentioned in the project description.
Nice to have
• We will leave the "nice to haves" to be decided by the designer.
Should not have
• Trees

```html
<!DOCTYPE html>
<html lang="en">
<head>
<meta charset="utf-8">
<title>Researcher Journey – Major Scientific Contributions</title>
<link rel="stylesheet" href="https://fonts.googleapis.com/css2?family=Carlito:wght@400;700&display=swap">
<style>
  :root {
    --teal: #3fa2a7;
    --navy: #1b3a60;
    --cream: #fbe8cd;
    --white: #ffffff;
    --award-red: #c0504d;
    --ink: #1a1a1a;
  }
  html, body {
    margin: 0;
    padding: 0;
    width: 1200px;
    height: 900px;
    overflow: hidden;
    background: var(--teal);
  }
  .journey {
    display: block;
    width: 1200px;
    height: 900px;
    font-family: "Carlito", "Calibri", sans-serif;
  }
  .journey__bg { fill: var(--teal); }
  .road { stroke: var(--navy); stroke-width: 11; stroke-linecap: round; fill: none; }
  .milestone { fill: var(--white); stroke: var(--navy); stroke-width: 5; }
  .branch { stroke: var(--navy); stroke-width: 1.4; fill: none; }
  .banner { fill: var(--cream); }
  .banner-label { fill: var(--ink); font-size: 15px; text-anchor: middle; dominant-baseline: middle; }
  .photo-frame { fill: var(--white); stroke: var(--navy); stroke-width: 6; }
  .photo-label { fill: var(--ink); font-size: 15px; text-anchor: middle; dominant-baseline: middle; }
  .award { fill: var(--award-red); }
  .award-label { fill: var(--white); font-size: 15px; text-anchor: middle; dominant-baseline: middle; }
  .destination { fill: var(--white); stroke: var(--navy); stroke-width: 9; }
  .destination-label { fill: var(--ink); font-size: 15px; text-anchor: middle; }
</style>
</head>
<body>
<svg class="journey" viewBox="0 0 720 540" xmlns="http://www.w3.org/2000/svg">
  <rect class="journey__bg" x="0" y="0" width="720" height="540"/>

  <!-- Main road -->
  <line class="road" x1="130" y1="152" x2="560" y2="405"/>

  <!-- Branch connectors -->
  <polyline class="branch" points="190,182 193,127 208,127 208,57 232,57"/>
  <polyline class="branch" points="252,218 275,218 275,149 290,149"/>
  <polyline class="branch" points="313,259 313,333 282,333"/>
  <polyline class="branch" points="377,295 350,295 350,415 332,415"/>
  <polyline class="branch" points="441,333 441,290 410,290 410,232 430,232"/>
  <polyline class="branch" points="508,372 485,372 485,495 463,495"/>

  <!-- Milestones on the road -->
  <circle class="milestone" cx="180" cy="182" r="8"/>
  <circle class="milestone" cx="247" cy="219" r="8"/>
  <circle class="milestone" cx="313" cy="259" r="8"/>
  <circle class="milestone" cx="377" cy="295" r="8"/>
  <circle class="milestone" cx="441" cy="333" r="8"/>
  <circle class="milestone" cx="508" cy="372" r="8"/>

  <!-- Contribution banners, right side (pointing left) -->
  <g class="contribution">
    <polygon class="banner" points="230,57 250,33 485,33 468,57 485,80 250,80"/>
    <text class="banner-label" x="362" y="58">Major Scientific Contribution</text>
  </g>
  <g class="contribution">
    <polygon class="banner" points="290,149 310,126 572,126 555,149 572,172 310,172"/>
    <text class="banner-label" x="433" y="150">Major Scientific Contribution</text>
  </g>
  <g class="contribution">
    <polygon class="banner" points="428,232 448,208 702,208 685,232 702,256 448,256"/>
    <text class="banner-label" x="566" y="233">Major Scientific Contribution</text>
  </g>

  <!-- Contribution banners, left side (pointing right) -->
  <g class="contribution">
    <polygon class="banner" points="8,311 262,311 282,334 262,357 8,357 24,334"/>
    <text class="banner-label" x="143" y="335">Major Scientific Contribution</text>
  </g>
  <g class="contribution">
    <polygon class="banner" points="62,393 312,393 332,416 312,440 62,440 78,416"/>
    <text class="banner-label" x="197" y="417">Major Scientific Contribution</text>
  </g>
  <g class="contribution">
    <polygon class="banner" points="193,472 443,472 463,495 443,519 193,519 209,495"/>
    <text class="banner-label" x="328" y="496">Major Scientific Contribution</text>
  </g>

  <!-- Researcher photo and award -->
  <rect class="photo-frame" x="25" y="16" width="108" height="142" role="img" aria-label="Researcher photo placeholder"/>
  <text class="photo-label" x="79" y="88">Photo</text>
  <rect class="award" x="22" y="160" width="114" height="50"/>
  <text class="award-label" x="79" y="181">Star Award</text>

  <!-- Destination -->
  <circle class="destination" cx="614" cy="446" r="80"/>
  <text class="destination-label" x="614" y="418">
    <tspan x="614" dy="0">Major</tspan>
    <tspan x="614" dy="21">Scientific</tspan>
    <tspan x="614" dy="21">Contribution</tspan>
  </text>
</svg>
</body>
</html>
```